Wordpress design for my private practice website - Psychotherapist

I would like a simple, clean, and elegant design for my private practice website. I work with both adults and children so I'd like it to appeal to both. However, since parents make the choice as to where to send their child for therapy, I want it to appeal to adults more. I would like the pictures on the site to have a calming effect - maybe using sand and water and rocks. I am attaching files with my company logo. I would also like my name incorporated into the header - Colette Brannigan, LCSW, Registered Play Therapist. I've also uploaded a picture of myself for my About Page.

I like the design of these 2 website and want something similar:
www.drlorapenwick.example
www.harwood-tallis.example

I would like a home page that highlights a calming graphic across the entire top of the page as well as my practice logo and my name.

I'd like a link to social media sites on the top of the homepage - facebook, pinterest.

I want a simple bar across the top with the following tabs:
Home
About Me (subtabs Who I Am, Specialties and Approach)
Counseling Services (subtabs Individual Counseling, Play Therapy, Sandplay Therapy,)
Fees
FAQs
Contact Me (would love this to be a fill in the blank contact form that sends info to my email address - should include name, phone number, email and a comment box for more information requested)
Blog (this will link with another wordpress blog)

Target Market(s)

Parents of children under age 12 with behavioral problems or are dealing with the breakup of their family through divorce - looking for someone to work with their young child. I also work with Adults that are overwhelmed and worried - often women that have many life stressors and are feeling burnt out on life and meeting everyone's needs. Families going through some type of trauma, including divorce or grief work. I also work with individuals going through a transition of religious beliefs - often exiting the religion of their youth and undergoing a crisis of faith at midlife.

Industry/Entity Type

Mental Health

Contact Information for Business Card

Colette Brannigan, LCSW
Registered Play Therapist
4917 Wexmoor Lane
Idaho Falls, Idaho 83404
(208)555-0187
www.stillbrookcounseling.example

On the opposite side, I'd like an appointment reminder area - with the following text:

Your next appointment is
_____/______/______ at ______am/pm
Please give 24 hrs notice if you need to cancel your appointment.

Coding

Coded - Design and coding required

Number of Pages Required

5+ page

Font styles to use
Sans Serif

Colors
33a6d7
9bcb3c
0355a3

Requirements
Must have
• I'd like it to be a wordpress site. I'm such a newby at web design - but I need to be able to add content and manage the site myself once it is up and running.
Nice to have
• I like the design of these 2 websites and want something similar:
• www.drlorapenwick.example
• www.harwood-tallis.example
• They are clean, easy to navigate and calming.
Should not have
• Should not look like a childcare website.

```html
<!DOCTYPE html>
<html lang="en">
<head>
<meta charset="utf-8">
<title>Stillbrook Counseling — About Maren Ashby</title>
<link rel="stylesheet" href="https://fonts.googleapis.com/css2?family=Cinzel:wght@700&family=Raleway:wght@200&family=Source+Sans+3:wght@400;600&display=swap">
<style>
  :root {
    --navy: #1f4f7d;
    --deep: #23557f;
    --teal: #267597;
    --nav-bg: rgba(110, 160, 185, 0.85);
    --frame: #8ea8c3;
    --green: #6a8a1c;
    --olive: #7a8f2a;
    --text: #333333;
    --white: #ffffff;
    --footer-link: #c6d6e6;
  }
  * { box-sizing: border-box; margin: 0; padding: 0; }
  html, body { width: 1200px; height: 1029px; overflow: hidden; background: var(--white); }
  body { position: relative; font-family: "Source Sans 3", sans-serif; color: var(--text); }

  .hero {
    position: absolute; left: 0; top: 0; width: 1200px; height: 189px;
    background: linear-gradient(180deg, #8a8ea6 0%, #c9a6a4 28%, #d9b9a3 38%, #9fb1bd 48%, #8fb0c1 70%, #6f97b1 100%);
  }
  .hero-stripe { position: absolute; left: 0; top: 189px; width: 1200px; height: 7px; background: var(--navy); }

  .brand {
    position: absolute; left: 189px; top: 76px; width: 184px;
    text-align: center; color: var(--white); font-weight: 600; text-transform: uppercase;
  }
  .brand-name { display: block; font-size: 19px; letter-spacing: 4px; line-height: 1; }
  .brand-sub { display: block; font-size: 9px; letter-spacing: 3px; margin-top: 6px; }

  .main-nav {
    position: absolute; left: 346px; top: 153px; width: 508px; height: 29px;
    background: var(--nav-bg); display: flex; justify-content: space-around; align-items: center;
    padding: 0 20px;
  }
  .main-nav a { color: var(--white); text-decoration: none; font-size: 12px; text-transform: uppercase; }

  .portrait-frame {
    position: absolute; left: 171px; top: 213px; width: 264px; height: 350px;
    border: 6px solid var(--frame); background: var(--white); padding: 0 5px 5px 0;
  }
  .portrait {
    width: 100%; height: 100%;
    background: linear-gradient(180deg, #f3f1ec 0%, #d8c08e 30%, #c9a77b 48%, #6f8a3a 70%, #4d6a2a 100%);
  }

  .bio { position: absolute; left: 469px; top: 218px; width: 504px; }
  .bio h1 {
    font-family: "Raleway", sans-serif; font-weight: 200; font-size: 38px; color: var(--navy);
    line-height: 1.2; padding-bottom: 6px; border-bottom: 1px solid var(--navy);
  }
  .bio p { font-size: 11.2px; line-height: 14.4px; width: 476px; margin-top: 14px; }
  .bio h1 + p { margin-top: 22px; }
  .bio .highlight { color: var(--green); }

  .service { position: absolute; top: 656px; width: 247px; text-align: center; }
  .service h2 {
    font-family: "Cinzel", serif; font-weight: 700; color: var(--navy);
    font-size: 25px; line-height: 1.1; letter-spacing: 0.5px;
  }
  .service h3 {
    font-family: "Cinzel", serif; font-weight: 700; color: var(--navy);
    font-size: 13px; letter-spacing: 7px; margin-top: 8px;
  }
  .service-box {
    margin-top: 16px; height: 138px; background: var(--teal); color: var(--white);
    text-align: left; font-size: 11.3px; line-height: 14.4px; padding: 16px 16px 0 17px;
  }
  .read-more {
    display: block; text-align: right; padding-right: 13px; margin-top: 9px;
    color: var(--navy); font-size: 13px; text-decoration: none;
  }
  .service--one { left: 198px; }
  .service--two { left: 481px; }
  .service--three { left: 764px; }
  .divider { position: absolute; top: 666px; width: 1px; height: 241px; background: var(--olive); }

  .footer-band { position: absolute; left: 0; top: 933px; width: 1200px; height: 12px; background: var(--teal); }
  .footer { position: absolute; left: 0; top: 945px; width: 1200px; height: 84px; background: var(--deep); }
  .footer-brand {
    position: absolute; left: 189px; top: 31px; color: var(--footer-link);
    font-weight: 600; text-transform: uppercase; text-align: center; width: 200px;
  }
  .footer-brand .brand-name { font-size: 15px; letter-spacing: 3px; }
  .footer-brand .brand-sub { font-size: 7.5px; letter-spacing: 2.5px; margin-top: 4px; }
  .footer-nav a {
    position: absolute; top: 35px; color: var(--footer-link); font-size: 12px;
    text-decoration: none; text-transform: uppercase;
  }
  .social { position: absolute; top: 26px; width: 33px; height: 33px; background: var(--olive); border-radius: 3px; }
</style>
</head>
<body>
  <header>
    <div class="hero" role="img" aria-label="Calm seascape at dusk with smooth rocks rising from still water"></div>
    <div class="hero-stripe"></div>
    <div class="brand">
      <span class="brand-name">Stillbrook</span>
      <span class="brand-sub">Counseling</span>
    </div>
    <nav class="main-nav">
      <a href="#">Home</a><a href="#">About</a><a href="#">Services</a><a href="#">FAQ</a><a href="#">Contact</a>
    </nav>
  </header>

  <main>
    <div class="portrait-frame">
      <div class="portrait" role="img" aria-label="Portrait photo of the therapist"></div>
    </div>

    <section class="bio">
      <h1>Maren Ashby</h1>
      <p>Lorem ipsum dolor sit amet consectetur adipiscing elit lorem ipsum dolor sit amet consectetur adipiscing elit lorem ipsum dolor sit amet consectetur adipiscing elit lorem ipsum dolor sit amet consectetur adipiscing elit lorem ipsum dolor sit amet consectetur adipiscing elit lorem ipsum dolor sit amet consectetur adipiscing elit lorem ipsum dolor sit amet consectetur adipiscing elit lorem ipsum dolor sit amet consectetur adipiscing elit.</p>
      <p>lorem ipsum dolor sit amet consectetur adipiscing elit lorem ipsum dolor sit amet consectetur adipiscing elit lorem ipsum dolor sit amet consectetur adipiscing elit lorem ipsum dolor sit amet consectetur adipiscing elit lorem ipsum dolor sit amet consectetur adipiscing elit lorem ipsum dolor sit amet consectetur adipiscing elit lorem ipsum dolor sit amet consectetur adipiscing elit lorem ipsum dolor sit amet consectetur adipiscing elit</p>
      <p class="highlight">lorem ipsum dolor sit amet consectetur adipiscing elit</p>
      <p>lorem ipsum dolor sit amet consectetur adipiscing elit lorem ipsum dolor sit amet consectetur adipiscing elit lorem ipsum dolor sit amet consectetur adipiscing elit lorem ipsum dolor sit amet consectetur adipiscing elit lorem ipsum dolor sit amet consectetur adipiscing elit lorem ipsum dolor sit amet consectetur adipiscing elit.</p>
    </section>

    <section class="service service--one">
      <h2>Counseling</h2>
      <h3>Services</h3>
      <div class="service-box">Lorem ipsum dolor sit amet consectetur adipiscing elit sit amet lorem ipsum dolor sit amet consectetur adipiscing elit sit und ipsum lorem sit amet ipsum elit und faq ipsum lorem sit amet.</div>
      <a class="read-more" href="#">Read more</a>
    </section>
    <div class="divider" style="left:463px"></div>
    <section class="service service--two">
      <h2>Lorem Ipsum</h2>
      <h3>Solutions</h3>
      <div class="service-box">Lorem ipsum dolor sit amet consectetur adipiscing elit sit amet lorem ipsum dolor sit amet consectetur adipiscing elit sit und ipsum lorem sit amet ipsum elit und faq ipsum lorem sit amet.</div>
      <a class="read-more" href="#">Read more</a>
    </section>
    <div class="divider" style="left:746px"></div>
    <section class="service service--three">
      <h2>Dolor Sit Amet</h2>
      <h3>Consulting</h3>
      <div class="service-box">Lorem ipsum dolor sit amet consectetur adipiscing elit sit amet lorem ipsum dolor sit amet consectetur adipiscing elit sit und ipsum lorem sit amet ipsum elit und faq ipsum lorem sit amet.</div>
      <a class="read-more" href="#">Read more</a>
    </section>
  </main>

  <div class="footer-band"></div>
  <footer class="footer">
    <div class="footer-brand">
      <span class="brand-name">Stillbrook</span>
      <span class="brand-sub">Counseling</span>
    </div>
    <nav class="footer-nav">
      <a href="#" style="left:485px">Home</a>
      <a href="#" style="left:555px">About</a>
      <a href="#" style="left:628px">Services</a>
      <a href="#" style="left:713px">FAQ</a>
      <a href="#" style="left:771px">Contact</a>
    </nav>
    <a class="social" href="#" style="left:926px" aria-label="Social profile"></a>
    <a class="social" href="#" style="left:976px" aria-label="Social profile"></a>
  </footer>
</body>
</html>
```